RIVERtide Press Needs a Book Cover Design

We need a book cover design for an inspirational, motivational nugget book. It's another part of a series of small 1-paragraph chapter books with lots of quotes. It is a spiritual book and we would like to see designs that depict peace through a storm. The final design should communicate peace or calm through violent storms of life--adversity, setbacks, and sorrow.
The book size is 5.5 x 8.5 ins and the number of pages is 96.
Updates
Project Deadline Extended
Reason: To be able to allow for more submissions.
Target Market(s)
General reading audience
Look and feel
Each slider illustrates characteristics of the customer's brand and the style your logo design should communicate.

```html
<!DOCTYPE html>
<html lang="en">
<head>
<meta charset="utf-8">
<title>Peace Through The Storms — Book Cover</title>
<link href="https://fonts.googleapis.com/css2?family=Cinzel:wght@400&family=Cormorant+Garamond:ital,wght@0,500;1,500&display=swap" rel="stylesheet">
<style>
  :root {
    --ink-light: #f3f1e4;
    --leaf-deep: #04120c;
    --leaf-green: #0a9a4c;
    --leaf-mid: #0c5a34;
    --teal-dark: #06302a;
    --teal-mid: #1a7a66;
    --teal-light: #3fb59b;
    --glow: #e4f6dc;
    --label-white: #ffffff;
  }
  html, body {
    margin: 0;
    padding: 0;
    width: 1200px;
    height: 899px;
    overflow: hidden;
    background: #000;
  }
  .cover-spread {
    position: relative;
    width: 1200px;
    height: 899px;
    overflow: hidden;
  }
  .back-cover {
    position: absolute;
    left: 0; top: 0;
    width: 590px; height: 899px;
    background:
      radial-gradient(ellipse 320px 440px at 430px 560px, var(--leaf-green) 0%, var(--leaf-mid) 55%, transparent 100%),
      radial-gradient(ellipse 380px 280px at 270px 320px, #0f5232 0%, transparent 100%),
      linear-gradient(160deg, #0a1a14 0%, var(--leaf-deep) 45%, #050a08 100%);
  }
  .front-cover {
    position: absolute;
    left: 590px; top: 0;
    width: 610px; height: 899px;
    background:
      radial-gradient(circle 120px at 196px 522px, var(--glow) 0%, rgba(140,210,180,0.6) 38%, transparent 100%),
      radial-gradient(ellipse 440px 400px at 290px 540px, var(--teal-light) 0%, var(--teal-mid) 50%, transparent 100%),
      radial-gradient(ellipse 260px 320px at 60px 160px, #050c0b 0%, transparent 100%),
      linear-gradient(170deg, #061a18 0%, var(--teal-dark) 30%, #0f5a4c 65%, #083a32 100%);
  }
  .label-box {
    position: absolute;
    left: 150px; top: 717px;
    width: 295px; height: 135px;
    background: var(--label-white);
  }
  .spine-title {
    position: absolute;
    left: 593px; top: 96px;
    writing-mode: vertical-rl;
    font-family: "Cormorant Garamond", "Times New Roman", serif;
    font-weight: 500;
    font-size: 20px;
    line-height: 1;
    color: var(--ink-light);
    white-space: nowrap;
    letter-spacing: 0.3px;
  }
  .title-block {
    position: absolute;
    left: 698px; top: 92px;
    margin: 0;
    font-weight: 400;
    color: var(--ink-light);
  }
  .title-main {
    display: block;
    font-family: "Cinzel", "Times New Roman", serif;
    font-size: 104px;
    line-height: 1;
    letter-spacing: 2px;
  }
  .title-sub {
    display: block;
    margin-top: 18px;
    font-family: "Cormorant Garamond", "Times New Roman", serif;
    font-style: italic;
    font-weight: 500;
    font-size: 60px;
    line-height: 1;
    white-space: nowrap;
  }
</style>
</head>
<body>
  <main class="cover-spread">
    <div class="back-cover" role="img" aria-label="Close-up of a curling green leaf in deep shadow"></div>
    <div class="label-box"></div>
    <div class="front-cover" role="img" aria-label="Glowing water droplet resting on a teal leaf, reflecting a dandelion"></div>
    <div class="spine-title">PEACE Through The Storms</div>
    <h1 class="title-block">
      <span class="title-main">PEACE</span>
      <span class="title-sub">Through The Storms</span>
    </h1>
  </main>
</body>
</html>
```